Infographic for B2B Service solution offering (sales funnel)

Attached is an example of something we need assistance with making into a more professional infographic. These infographics are for our B2B marketing services, aimed at IT Consulting firms.

We have done some basic graphics (attached) and this will provide you guidance (video link on google sheet):
https://pages.vardolink.net/sheet/r/7kQm3TzP9wLcYe2HbNvAsDxR4uFgJ8tWoZiE6yKpBq/view?mode=shared

Here are some examples you can model for the new infographic:
https://vault.vardolink.net/store/groups/48PkTwMz3nRq9LbXvYc-hsd2FjQe?ref=store_link

Target Market(s)

B2B IT Consulting Firms

Industry/Entity Type

Information Technology, Consulting

Colors

Designer to choose colors to be used in the design.

Requirements
Must have
• professional, high level consulting firms are target market
Should not have
• cartoonish

```html
<!DOCTYPE html>
<html lang="en">
<head>
<meta charset="utf-8">
<title>B2B Relationship Funnel Infographic</title>
<link href="https://fonts.googleapis.com/css2?family=Lato:wght@400;700;900&display=swap" rel="stylesheet">
<style>
  :root {
    --page: #ffffff;
    --panel: #f2efea;
    --ink: #1d3a3f;
    --ribbon: #3f7f78;
    --referral: #c9561b;
    --referral-soft: #e3a887;
    --trust-green: #3a8f6b;
    --white: #ffffff;
  }
  html, body {
    margin: 0;
    padding: 0;
    width: 829px;
    height: 1200px;
    overflow: hidden;
    background: var(--page);
    font-family: "Lato", sans-serif;
  }
  .canvas { position: relative; width: 829px; height: 1200px; }
  .panel {
    position: absolute;
    width: 353px;
    height: 353px;
    background: var(--panel);
  }
  .panel svg { display: block; width: 353px; height: 353px; }
  .p-relationships { left: 63px; top: 60px; }
  .p-b2b { left: 421px; top: 60px; }
  .p-agency { left: 63px; top: 418px; }
  .p-method { left: 421px; top: 418px; }
  .p-blank { left: 63px; top: 776px; }

  .title { font-family: "Lato", sans-serif; font-weight: 700; font-size: 34px; fill: var(--ink); text-anchor: middle; }
  .stage-top { font-weight: 900; font-size: 18px; fill: var(--ink); text-anchor: middle; }
  .trust-label { font-weight: 700; font-size: 10.5px; fill: var(--ink); text-anchor: end; }
  .trust-dots { stroke: url(#gTrust); stroke-width: 6; stroke-dasharray: 0 10; stroke-linecap: round; fill: none; }
  .trust-arrow { fill: var(--trust-green); }

  .tier-dark .body { fill: url(#gDarkBody); }
  .tier-dark .top { fill: url(#gDarkTop); }
  .tier-lead .top { fill: #3e6a70; }
  .tier-light .body { fill: url(#gLightBody); }
  .tier-light .top { fill: url(#gLightTop); }
  .tier-faded .body { fill: url(#gFadedBody); }
  .tier-faded .top { fill: url(#gFadedTop); }

  .tier-label { font-weight: 900; font-size: 17px; fill: var(--white); text-anchor: middle; letter-spacing: -0.2px; }
  .tier-faded .tier-label { fill: #f4f5f4; }

  .ribbon { fill: var(--ribbon); }
  .ribbon-text { font-weight: 700; font-size: 10.5px; fill: var(--white); }

  .referral-box { fill: var(--referral); }
  .referral-line { stroke: var(--referral); stroke-width: 2; }
  .referral-dot { fill: var(--referral); }
  .referral-soft .referral-box { fill: var(--referral-soft); }
  .referral-soft .referral-line { stroke: var(--referral-soft); }
  .referral-soft .referral-dot { fill: var(--referral-soft); }
  .referral-text { font-weight: 900; font-size: 12px; fill: var(--white); text-anchor: middle; }
  .referral-text.small { font-size: 7px; }

  .shortcut-line { stroke: var(--ribbon); stroke-width: 2; stroke-dasharray: 4 4; fill: none; }
  .shortcut-head { fill: var(--ribbon); }
  .shortcut-label { font-weight: 700; font-size: 11px; fill: var(--ink); text-anchor: middle; }
  .flow-mark { stroke: var(--ink); stroke-width: 1.5; fill: none; }
</style>
</head>
<body>
<svg width="0" height="0" style="position:absolute" aria-hidden="true">
  <defs>
    <linearGradient id="gDarkBody" x1="0" y1="0" x2="1" y2="0">
      <stop offset="0" stop-color="#3f6d73"/>
      <stop offset="0.55" stop-color="#2a5359"/>
      <stop offset="1" stop-color="#132f35"/>
    </linearGradient>
    <radialGradient id="gDarkTop" cx="0.5" cy="0.6" r="0.6">
      <stop offset="0" stop-color="#14262a"/>
      <stop offset="1" stop-color="#3d686e"/>
    </radialGradient>
    <linearGradient id="gLightBody" x1="0" y1="0" x2="1" y2="0">
      <stop offset="0" stop-color="#a2b1b0"/>
      <stop offset="0.55" stop-color="#7d8f90"/>
      <stop offset="1" stop-color="#485b5e"/>
    </linearGradient>
    <radialGradient id="gLightTop" cx="0.5" cy="0.6" r="0.6">
      <stop offset="0" stop-color="#263538"/>
      <stop offset="1" stop-color="#9eadad"/>
    </radialGradient>
    <linearGradient id="gFadedBody" x1="0" y1="0" x2="1" y2="0">
      <stop offset="0" stop-color="#c8cfce"/>
      <stop offset="0.6" stop-color="#a8b3b3"/>
      <stop offset="1" stop-color="#8a9899"/>
    </linearGradient>
    <radialGradient id="gFadedTop" cx="0.5" cy="0.6" r="0.6">
      <stop offset="0" stop-color="#9aa5a5"/>
      <stop offset="1" stop-color="#d3d9d8"/>
    </radialGradient>
    <linearGradient id="gTrust" gradientUnits="userSpaceOnUse" x1="0" y1="180" x2="0" y2="600">
      <stop offset="0" stop-color="#d6203f"/>
      <stop offset="0.3" stop-color="#ee7b3c"/>
      <stop offset="0.5" stop-color="#f1dc4a"/>
      <stop offset="0.72" stop-color="#9cc25a"/>
      <stop offset="1" stop-color="#2f8a63"/>
    </linearGradient>
  </defs>
</svg>

<main class="canvas">

  <!-- Personal relationships -->
  <section class="panel p-relationships">
    <svg viewBox="0 0 679 680">
      <text class="title" x="340" y="97">How Relationships are Built</text>
      <text class="stage-top" x="340" y="157">COLD LEADS</text>
      <text class="trust-label" x="155" y="192">LOW</text>
      <text class="trust-label" x="155" y="204">TRUST</text>
      <text class="trust-label" x="155" y="585">HIGH</text>
      <text class="trust-label" x="155" y="597">TRUST</text>
      <line class="trust-dots" x1="175" y1="180" x2="175" y2="590"/>
      <path class="trust-arrow" d="M164 596 L175 606 L186 596 L186 601 L175 612 L164 601 Z"/>

      <g class="tier tier-dark tier-lead"><path class="body" d="M216 183 L226 219 A110 14 0 0 0 446 219 L456 183 Z"/><ellipse class="top" cx="336" cy="183" rx="120" ry="14"/><text class="tier-label" x="336" y="221">PHONE #</text></g>
      <g class="tier tier-light"><path class="body" d="M224.5 247 L234.5 283 A101.5 14 0 0 0 437.5 283 L447.5 247 Z"/><ellipse class="top" cx="336" cy="247" rx="111.5" ry="14"/><text class="tier-label" x="336" y="285">COFFEE</text></g>
      <g class="tier tier-dark"><path class="body" d="M233 311 L243 347 A93 14 0 0 0 429 347 L439 311 Z"/><ellipse class="top" cx="336" cy="311" rx="103" ry="14"/><text class="tier-label" x="336" y="349">DINNER</text></g>
      <g class="tier tier-light"><path class="body" d="M241.5 375 L251.5 411 A84.5 14 0 0 0 420.5 411 L430.5 375 Z"/><ellipse class="top" cx="336" cy="375" rx="94.5" ry="14"/><text class="tier-label" x="336" y="413">WEEKEND TRAVEL</text></g>
      <g class="tier tier-dark"><path class="body" d="M250 439 L260 475 A76 14 0 0 0 412 475 L422 439 Z"/><ellipse class="top" cx="336" cy="439" rx="86" ry="14"/><text class="tier-label" x="336" y="477">MEET PARENTS</text></g>
      <g class="tier tier-light"><path class="body" d="M258.5 503 L268.5 539 A67.5 14 0 0 0 403.5 539 L413.5 503 Z"/><ellipse class="top" cx="336" cy="503" rx="77.5" ry="14"/><text class="tier-label" x="336" y="541">MOVE IN</text></g>
      <g class="tier tier-dark"><path class="body" d="M267 567 L277 603 A59 14 0 0 0 395 603 L405 567 Z"/><ellipse class="top" cx="336" cy="567" rx="69" ry="14"/><text class="tier-label" x="336" y="605">WIFE</text></g>

      <g class="offers">
        <path class="ribbon" d="M409 232 L419 223 L641 223 L638 241 L419 241 Z"/><text class="ribbon-text" x="423" y="236">Offer #1: Low Risk, Low Investment</text>
        <path class="ribbon" d="M401 297 L411 288 L633 288 L630 306 L411 306 Z"/><text class="ribbon-text" x="415" y="301">Offer #2: Low Risk, Medium Investment</text>
        <path class="ribbon" d="M393 362 L403 353 L625 353 L622 371 L403 371 Z"/><text class="ribbon-text" x="407" y="366">Offer #3: Medium Risk, Medium Investment</text>
        <path class="ribbon" d="M385 427 L395 418 L617 418 L614 436 L395 436 Z"/><text class="ribbon-text" x="399" y="431">Offer #4: High Risk, Medium Investment</text>
        <path class="ribbon" d="M377 492 L387 483 L609 483 L606 501 L387 501 Z"/><text class="ribbon-text" x="391" y="496">Offer #5: Medium Risk, High Investment</text>
        <path class="ribbon" d="M369 557 L379 548 L601 548 L598 566 L379 566 Z"/><text class="ribbon-text" x="383" y="561">Offer #6: High Risk, High Investment</text>
        <path class="ribbon" d="M361 622 L371 613 L593 613 L590 631 L371 631 Z"/><text class="ribbon-text" x="375" y="626">Offer #7: High Risk, High Investment</text>
      </g>
    </svg>
  </section>

  <!-- B2B relationships -->
  <section class="panel p-b2b">
    <svg viewBox="0 0 679 680">
      <text class="title" x="340" y="97">How B2B Relationships are Built</text>
      <text class="trust-label" x="155" y="200">LOW</text>
      <text class="trust-label" x="155" y="212">TRUST</text>
      <text class="trust-label" x="155" y="553">HIGH</text>
      <text class="trust-label" x="155" y="565">TRUST</text>
      <line class="trust-dots" x1="175" y1="190" x2="175" y2="550"/>
      <path class="trust-arrow" d="M164 556 L175 566 L186 556 L186 561 L175 572 L164 561 Z"/>

      <path class="shortcut-line" d="M412 165 L500 165 Q507 165 507 172 L507 388"/>
      <path class="shortcut-head" d="M404 165 L412 161 L412 169 Z"/>
      <path class="shortcut-head" d="M503 388 L511 388 L507 396 Z"/>
      <text class="shortcut-label" x="507" y="286">SHORTCUT</text>

      <g transform="translate(0,12)">
        <text class="stage-top" x="340" y="157">COLD LEADS</text>
        <g class="tier tier-dark tier-lead"><path class="body" d="M216 183 L226 219 A110 14 0 0 0 446 219 L456 183 Z"/><ellipse class="top" cx="336" cy="183" rx="120" ry="14"/><text class="tier-label" x="336" y="221">RESPONSE</text></g>
        <g class="tier tier-light"><path class="body" d="M224.5 247 L234.5 283 A101.5 14 0 0 0 437.5 283 L447.5 247 Z"/><ellipse class="top" cx="336" cy="247" rx="111.5" ry="14"/><text class="tier-label" x="336" y="285">FIRST CONVERSATION</text></g>
        <g class="tier tier-dark"><path class="body" d="M233 311 L243 347 A93 14 0 0 0 429 347 L439 311 Z"/><ellipse class="top" cx="336" cy="311" rx="103" ry="14"/><text class="tier-label" x="336" y="349">TRUST BUILDING</text></g>
        <g class="tier tier-light"><path class="body" d="M241.5 375 L251.5 411 A84.5 14 0 0 0 420.5 411 L430.5 375 Z"/><ellipse class="top" cx="336" cy="375" rx="94.5" ry="14"/><text class="tier-label" x="336" y="413">PROBLEM AWARE</text></g>
        <g class="tier tier-dark"><path class="body" d="M250 439 L260 475 A76 14 0 0 0 412 475 L422 439 Z"/><ellipse class="top" cx="336" cy="439" rx="86" ry="14"/><text class="tier-label" x="336" y="477">INTENT</text></g>
        <g class="tier tier-light"><path class="body" d="M258.5 503 L268.5 539 A67.5 14 0 0 0 403.5 539 L413.5 503 Z"/><ellipse class="top" cx="336" cy="503" rx="77.5" ry="14"/><text class="tier-label" x="336" y="541">CUSTOMER</text></g>
      </g>

      <g class="referral">
        <line class="referral-line" x1="420" y1="411" x2="464" y2="411"/>
        <circle class="referral-dot" cx="421" cy="411" r="3"/>
        <circle class="referral-dot" cx="461" cy="411" r="3"/>
        <rect class="referral-box" x="464" y="393" width="86" height="36" rx="5"/>
        <text class="referral-text" x="507" y="408">REFERRAL</text>
        <text class="referral-text" x="507" y="421">PROSPECT</text>
      </g>
    </svg>
  </section>

  <!-- Typical agency -->
  <section class="panel p-agency">
    <svg viewBox="0 0 679 680">
      <text class="title" x="340" y="97">Typical Marketing Agency</text>
      <text class="trust-label" x="155" y="200">LOW</text>
      <text class="trust-label" x="155" y="212">TRUST</text>
      <text class="trust-label" x="155" y="553">HIGH</text>
      <text class="trust-label" x="155" y="565">TRUST</text>
      <line class="trust-dots" x1="175" y1="190" x2="175" y2="550"/>
      <path class="trust-arrow" d="M164 556 L175 566 L186 556 L186 561 L175 572 L164 561 Z"/>

      <g transform="translate(0,12)">
        <text class="stage-top" x="340" y="157">COLD LEADS</text>
        <g class="tier tier-light tier-faded"><path class="body" d="M224.5 247 L234.5 283 A101.5 14 0 0 0 437.5 283 L447.5 247 Z"/><ellipse class="top" cx="336" cy="247" rx="111.5" ry="14"/><text class="tier-label" x="336" y="285">FIRST CONVERSATION</text></g>
        <g class="tier tier-light tier-faded"><path class="body" d="M233 311 L243 347 A93 14 0 0 0 429 347 L439 311 Z"/><ellipse class="top" cx="336" cy="311" rx="103" ry="14"/><text class="tier-label" x="336" y="349">TRUST BUILDING</text></g>
        <g class="tier tier-light tier-faded"><path class="body" d="M241.5 375 L251.5 411 A84.5 14 0 0 0 420.5 411 L430.5 375 Z"/><ellipse class="top" cx="336" cy="375" rx="94.5" ry="14"/><text class="tier-label" x="336" y="413">PROBLEM AWARE</text></g>
        <g class="tier tier-light tier-faded"><path class="body" d="M250 439 L260 475 A76 14 0 0 0 412 475 L422 439 Z"/><ellipse class="top" cx="336" cy="439" rx="86" ry="14"/><text class="tier-label" x="336" y="477">INTENT</text></g>
        <g class="tier tier-light tier-faded"><path class="body" d="M258.5 503 L268.5 539 A67.5 14 0 0 0 403.5 539 L413.5 503 Z"/><ellipse class="top" cx="336" cy="503" rx="77.5" ry="14"/><text class="tier-label" x="336" y="541">CUSTOMER</text></g>
        <g class="tier tier-dark tier-lead"><path class="body" d="M216 183 L226 219 A110 14 0 0 0 446 219 L456 183 Z"/><ellipse class="top" cx="336" cy="183" rx="120" ry="14"/><text class="tier-label" x="336" y="221">RESPONSE</text></g>
        <path class="flow-mark" d="M340 163 L340 185 M336 167 L340 162 L344 167 M336 181 L340 186 L344 181"/>
      </g>

      <g class="referral referral-soft">
        <line class="referral-line" x1="420" y1="411" x2="464" y2="411"/>
        <circle class="referral-dot" cx="421" cy="411" r="3"/>
        <circle class="referral-dot" cx="461" cy="411" r="3"/>
        <rect class="referral-box" x="464" y="393" width="86" height="36" rx="5"/>
        <text class="referral-text" x="507" y="408">REFERRAL</text>
        <text class="referral-text" x="507" y="421">PROSPECT</text>
      </g>
    </svg>
  </section>

  <!-- Method -->
  <section class="panel p-method">
    <svg viewBox="0 0 679 680">
      <text class="title" x="340" y="93">The Trust Ladder Approach</text>
      <text class="trust-label" x="144" y="200">LOW</text>
      <text class="trust-label" x="144" y="212">TRUST</text>
      <text class="trust-label" x="144" y="553">HIGH</text>
      <text class="trust-label" x="144" y="565">TRUST</text>
      <line class="trust-dots" x1="163" y1="190" x2="163" y2="550"/>
      <path class="trust-arrow" d="M152 556 L163 566 L174 556 L174 561 L163 572 L152 561 Z"/>

      <g transform="translate(0,12)">
        <text class="stage-top" x="340" y="157">COLD LEADS</text>
        <g class="tier tier-dark tier-lead"><path class="body" d="M216 183 L226 219 A110 14 0 0 0 446 219 L456 183 Z"/><ellipse class="top" cx="336" cy="183" rx="120" ry="14"/><text class="tier-label" x="336" y="221">RESPONSE</text></g>
        <g class="tier tier-light"><path class="body" d="M224.5 247 L234.5 283 A101.5 14 0 0 0 437.5 283 L447.5 247 Z"/><ellipse class="top" cx="336" cy="247" rx="111.5" ry="14"/><text class="tier-label" x="336" y="285">FIRST CONVERSATION</text></g>
        <g class="tier tier-dark"><path class="body" d="M233 311 L243 347 A93 14 0 0 0 429 347 L439 311 Z"/><ellipse class="top" cx="336" cy="311" rx="103" ry="14"/><text class="tier-label" x="336" y="349">TRUST BUILDING</text></g>
        <g class="tier tier-light"><path class="body" d="M241.5 375 L251.5 411 A84.5 14 0 0 0 420.5 411 L430.5 375 Z"/><ellipse class="top" cx="336" cy="375" rx="94.5" ry="14"/><text class="tier-label" x="336" y="413">PROBLEM AWARE</text></g>
        <g class="tier tier-dark"><path class="body" d="M250 439 L260 475 A76 14 0 0 0 412 475 L422 439 Z"/><ellipse class="top" cx="336" cy="439" rx="86" ry="14"/><text class="tier-label" x="336" y="477">INTENT</text></g>
        <g class="tier tier-light"><path class="body" d="M258.5 503 L268.5 539 A67.5 14 0 0 0 403.5 539 L413.5 503 Z"/><ellipse class="top" cx="336" cy="503" rx="77.5" ry="14"/><text class="tier-label" x="336" y="541">CUSTOMER</text></g>
      </g>

      <g class="offers">
        <path class="ribbon" d="M386 252 L396 243 L615 243 L612 261 L396 261 Z"/><text class="ribbon-text" x="400" y="256">Offer #1: Low Risk, Low Investment</text>
        <path class="ribbon" d="M378 317 L388 308 L607 308 L604 326 L388 326 Z"/><text class="ribbon-text" x="392" y="321">Offer #2: Low Risk, Medium Investment</text>
        <path class="ribbon" d="M370 382 L380 373 L599 373 L596 391 L380 391 Z"/><text class="ribbon-text" x="384" y="386">Offer #3: Medium Risk, Medium Investment</text>
        <path class="ribbon" d="M362 447 L372 438 L591 438 L588 456 L372 456 Z"/><text class="ribbon-text" x="376" y="451">Offer #4: High Risk, High Investment</text>
        <path class="ribbon" d="M354 512 L364 503 L583 503 L580 521 L364 521 Z"/><text class="ribbon-text" x="368" y="516">Offer #5: High Risk, High Investment</text>
        <path class="ribbon" d="M346 577 L356 568 L575 568 L572 586 L356 586 Z"/><text class="ribbon-text" x="360" y="581">Core Offer: Medium Risk, High Investment</text>
      </g>

      <g class="referral">
        <line class="referral-line" x1="236" y1="414" x2="256" y2="414"/>
        <circle class="referral-dot" cx="255" cy="414" r="2.5"/>
        <rect class="referral-box" x="181" y="403" width="55" height="22" rx="3"/>
        <text class="referral-text small" x="208.5" y="413">REFERRAL</text>
        <text class="referral-text small" x="208.5" y="421">PROSPECT</text>
      </g>
    </svg>
  </section>

  <!-- Unlabelled funnel -->
  <section class="panel p-blank">
    <svg viewBox="0 0 679 680">
      <text class="trust-label" x="155" y="200">LOW</text>
      <text class="trust-label" x="155" y="212">TRUST</text>
      <text class="trust-label" x="155" y="553">HIGH</text>
      <text class="trust-label" x="155" y="565">TRUST</text>
      <line class="trust-dots" x1="175" y1="190" x2="175" y2="550"/>
      <path class="trust-arrow" d="M164 556 L175 566 L186 556 L186 561 L175 572 L164 561 Z"/>

      <g transform="translate(0,12)">
        <text class="stage-top" x="340" y="157">COLD LEADS</text>
        <g class="tier tier-dark tier-lead"><path class="body" d="M216 183 L226 219 A110 14 0 0 0 446 219 L456 183 Z"/><ellipse class="top" cx="336" cy="183" rx="120" ry="14"/></g>
        <g class="tier tier-light"><path class="body" d="M224.5 247 L234.5 283 A101.5 14 0 0 0 437.5 283 L447.5 247 Z"/><ellipse class="top" cx="336" cy="247" rx="111.5" ry="14"/></g>
        <g class="tier tier-dark"><path class="body" d="M233 311 L243 347 A93 14 0 0 0 429 347 L439 311 Z"/><ellipse class="top" cx="336" cy="311" rx="103" ry="14"/></g>
        <g class="tier tier-light"><path class="body" d="M241.5 375 L251.5 411 A84.5 14 0 0 0 420.5 411 L430.5 375 Z"/><ellipse class="top" cx="336" cy="375" rx="94.5" ry="14"/></g>
        <g class="tier tier-dark"><path class="body" d="M250 439 L260 475 A76 14 0 0 0 412 475 L422 439 Z"/><ellipse class="top" cx="336" cy="439" rx="86" ry="14"/></g>
        <g class="tier tier-light"><path class="body" d="M258.5 503 L268.5 539 A67.5 14 0 0 0 403.5 539 L413.5 503 Z"/><ellipse class="top" cx="336" cy="503" rx="77.5" ry="14"/></g>
      </g>
    </svg>
  </section>

</main>
</body>
</html>
```